Lunaryth needs a elegant mystical business card design

The theme of Lunaryth is centered on Kemetic/Ancient Egyptian Spirituality. My business sells handmade scented candles, mystic oils, body sprays, tarot readings and more. I would like my business card to reflect an elegant and mystical look. Hieroglyphs around the borders would be a cool idea. Also, the main colors I am working with is Black and Gold= colors of royalty. Black background. The business card will be double sided. The back will have the logo, and the front will have the basic information (ie name, title, business, phone, email, website, etc..)

Target Market(s)

The target market are people into metaphysics, holistic healing, ancient Egyptian culture, aromatherapy, occult science, and the esoteric.

Industry/Entity Type

Business

Contact Information for Business Card

Name: Marisol T. Pike
Title: Owner
Business: LUNARYTH
Phone: 555.210.4473
Website: www.Lunaryth.example
Facebook, Instagram, and twitter icons

Font styles to use
Serif
Decorative

Requirements
Must have
• My logo, and website.
Nice to have
• Ancient Egyptian hieroglyphs, Elegant designs around the border, or encircling the logo.

```html
<!DOCTYPE html>
<html lang="en">
<head>
<meta charset="utf-8">
<title>Lunaryth Business Card</title>
<link href="https://fonts.googleapis.com/css2?family=Open+Sans:wght@400;600;700&display=swap" rel="stylesheet">
<style>
  :root {
    --backdrop: #7a4e33;
    --card-black: #050505;
    --panel-black: #111111;
    --gold: #b8945a;
    --gold-light: #d7b77c;
    --glyph-band: #4a3a22;
    --glyph-band-soft: #5e4a2c;
    --white: #ffffff;
  }
  * { box-sizing: border-box; margin: 0; padding: 0; }
  html, body {
    width: 1200px; height: 1000px; overflow: hidden;
    background: var(--backdrop);
    font-family: "Open Sans", Arial, sans-serif;
  }
  .card {
    position: absolute; left: 265px; width: 694px; height: 398px;
    background: var(--card-black);
    box-shadow: 0 4px 14px rgba(0,0,0,0.45);
    overflow: hidden;
  }
  .card--front { top: 72px; }
  .card--back { top: 533px; }

  .hieroglyph-border {
    position: absolute; inset: 8px 6px 6px 6px;
    border-style: solid;
    border-width: 34px 38px 34px 36px;
    border-image: linear-gradient(135deg, var(--glyph-band), var(--glyph-band-soft), var(--glyph-band)) 1;
    z-index: 2;
  }
  .info-panel {
    position: absolute; left: 70px; top: 12px; width: 525px; height: 316px;
    background: var(--panel-black);
    z-index: 1;
  }
  .content { position: absolute; inset: 0; z-index: 3; text-align: center; }

  .brand-name {
    position: absolute; left: 0; right: 0;
    font-weight: 600; color: var(--gold);
    letter-spacing: 6px;
  }
  .card--front .brand-name { top: 100px; font-size: 30px; }
  .card--back .brand-name { top: 160px; font-size: 36px; }

  .person-name {
    position: absolute; left: 0; right: 0; top: 216px;
    color: var(--white); font-weight: 700; font-size: 17px; letter-spacing: 0.5px;
  }
  .person-title {
    position: absolute; left: 0; right: 0; top: 239px;
    color: var(--gold); font-size: 15px;
  }
  .divider {
    position: absolute; left: 150px; right: 150px; top: 268px; height: 1px;
    background: linear-gradient(90deg, transparent, #3a3a3a, transparent);
  }
  .contact-line {
    position: absolute; left: 0; right: 0; top: 280px;
    color: var(--white); font-size: 15px;
  }
  .contact-line .label { color: var(--gold); font-weight: 700; margin-right: 4px; }
  .contact-line .sep { color: var(--gold); margin: 0 6px; }
  .social-links {
    position: absolute; left: 0; right: 0; top: 315px;
    display: flex; justify-content: center; gap: 12px;
  }
  .social-links span {
    width: 18px; height: 18px; border-radius: 3px; background: var(--gold);
  }
  .website {
    position: absolute; left: 0; right: 0; top: 314px;
    color: var(--white); font-size: 16px; letter-spacing: 0.3px;
  }
  .website b { font-weight: 700; }
</style>
</head>
<body>

<section class="card card--front">
  <div class="info-panel"></div>
  <div class="hieroglyph-border" role="img" aria-label="Border of gold Egyptian hieroglyphs"></div>
  <div class="content">
    <div class="brand-name">LUNARYTH</div>
    <div class="person-name">MARISOL T. PIKE</div>
    <div class="person-title">Owner</div>
    <div class="divider"></div>
    <div class="contact-line">
      <span class="label">T</span>555.210.4473<span class="sep">|</span><span class="label">E</span>marisol@lunaryth.example
    </div>
    <div class="social-links" role="img" aria-label="Social media links">
      <span></span><span></span><span></span>
    </div>
  </div>
</section>

<section class="card card--back">
  <div class="hieroglyph-border" role="img" aria-label="Border of gold Egyptian hieroglyphs"></div>
  <div class="content">
    <div class="brand-name">LUNARYTH</div>
    <div class="website">www.<b>Lunaryth</b>.example</div>
  </div>
</section>

</body>
</html>
```